Wordpress Site Design for a Horror and Action Movie Production Company

We need a re-design/facelift of our website: https://q7zk.pagecraftr-demo.net
The structure of the website could remain the same, but it needs to look and feel BETTER!

We would like the website coded in Wordpress so that it can be easily updated bu us, via adding new projects and new projects' info.

We specialize in Action, Horror, and Sci-Fi Genre. That being said, we don't want the website to look like it's a themed park with haunted houses. It should still be sharp and professional, as after all - it is a business for us!

Target Market(s)

Film Distribution Companies (B2B), as well as general audience that likes movies

Industry/Entity Type

Movie Production

Coding

Coded - Design and coding required

Number of Pages Required

5+ page

Font styles to use
Sans Serif

Colors

Designer to choose colors to be used in the design.

Requirements
Must have
• - PROJECTS page
• - Each PROJECT has a sub-page with project info/updates (up dates could be in a form of a WP post, ideally a template that we can use to update and create new PROJECT pages, with text, poster, and video link (trailer))
• - NEWS page that chronologically lists updates from all PROJECTS (could be done via WP blog)
• - HOME page would
Nice to have
• Should generally have a dark background.
• Websites we like as a reference of general approach and style:
• https://marlowvexla.com
• https://tuvakreel.com (however this is very image-centric, and we might not have that much imagery at the moment)
• https://www.pebblecreeklightandframe.com/other
• https://kelvapics.com
Should not have
• We specialize in Action, Horror, and Sci-Fi Genre. That being said, we don't want the website to look like it's a themed park with haunted houses. It should still be sharp and professional, as after all - it is a business for us!

```html
<!DOCTYPE html>
<html lang="en">
<head>
<meta charset="utf-8">
<title>Quarry 9 Pictures</title>
<link rel="stylesheet" href="https://fonts.googleapis.com/css2?family=Montserrat:wght@300;400;500;600;700;900&family=Great+Vibes&display=swap">
<style>
:root{
  --red:#e8141c;
  --ink:#1d1d1f;
  --text:#6c6c72;
  --muted:#a5a5aa;
  --line:#e6e6e9;
  --footer:#231f20;
  --footer-deep:#1a1718;
  --white:#ffffff;
}
*{box-sizing:border-box;margin:0;padding:0}
html,body{width:1200px;height:3588px;overflow:hidden}
body{position:relative;background:var(--white);font-family:"Montserrat",Arial,sans-serif;color:var(--ink)}
.abs{position:absolute}

/* header */
.brand{left:32px;top:28px;width:188px;height:96px;background:var(--ink);display:flex;align-items:center;justify-content:center;color:var(--white);font-weight:700;font-size:19px;letter-spacing:1px;text-transform:uppercase}
.nav{right:248px;top:66px;display:flex;gap:36px;font-size:15px;color:var(--ink)}
.nav-cta{left:1030px;top:58px;width:140px;height:40px;border-radius:20px;background:var(--red);color:var(--white);font-size:14px;font-weight:600;display:flex;align-items:center;justify-content:center}

/* hero */
.hero-count{left:0;width:1200px;top:150px;text-align:center;font-weight:900;font-size:250px;letter-spacing:-10px;line-height:1;
  background:linear-gradient(100deg,#3a2a1e 0%,#b38a4c 25%,#f0c060 40%,#7a5a38 60%,#2e2a28 80%,#9a7a5a 100%);
  -webkit-background-clip:text;background-clip:text;color:transparent}
.hero-plus{left:760px;top:210px;width:150px;height:150px;border-radius:50%;background:var(--red);color:var(--white);font-size:110px;font-weight:300;display:flex;align-items:center;justify-content:center;line-height:1}
.section-label{left:0;width:1200px;text-align:center;font-size:40px;font-weight:400;color:var(--ink)}

/* project tiles */
.tile{box-shadow:0 10px 24px rgba(0,0,0,.25)}
.tile .play{position:absolute;left:50%;top:50%;width:30px;height:30px;margin:-15px 0 0 -15px;border-radius:50%;background:var(--white)}
.tile .play::after{content:"";position:absolute;left:12px;top:9px;border-left:9px solid var(--ink);border-top:6px solid transparent;border-bottom:6px solid transparent}

/* about */
.about-map{left:300px;top:1150px;width:760px;height:420px;background:radial-gradient(ellipse at center,#f2f2f4 0%,#fbfbfc 60%,transparent 75%)}
.heading{font-size:64px;font-weight:300;color:var(--ink)}
.script{font-family:"Great Vibes",cursive;color:var(--red);font-size:84px;font-weight:400}
.about-title{left:0;width:1200px;top:1200px;text-align:center}
.about-copy{left:192px;width:800px;font-size:17px;line-height:30px;color:var(--text)}

/* services */
.crew-photo{left:0;top:1640px;width:600px;height:480px;background:linear-gradient(135deg,#e9d6b0 0%,#b99066 35%,#5d4a3c 70%,#2e2620 100%)}
.services-title{left:664px;top:1690px;width:400px;font-size:22px;font-weight:700;line-height:30px}
.skill{left:664px;width:400px}
.skill-name{font-size:12px;color:var(--ink)}
.skill-track{margin-top:12px;height:2px;background:var(--line);position:relative}
.skill-fill{position:absolute;left:0;top:0;height:2px;background:var(--red)}
.btn{background:var(--red);color:var(--white);border-radius:20px;font-size:12px;font-weight:600;display:flex;align-items:center;justify-content:center}

/* founders */
.founders-title{left:0;width:1200px;top:2225px;text-align:center}
.founder{top:2340px;width:256px;height:256px;box-shadow:0 8px 22px rgba(0,0,0,.2)}
.founder-name{position:absolute;left:0;right:0;bottom:30px;text-align:center;color:var(--white);font-size:24px;font-weight:600}
.founder-role{position:absolute;left:0;right:0;bottom:14px;text-align:center;color:var(--white);font-size:11px}
.arrow{top:2456px;width:32px;height:32px;border:1px solid var(--line);border-radius:50%;display:flex;align-items:center;justify-content:center;color:var(--ink);font-size:14px}

/* quote */
.quote-title{left:192px;top:2755px;font-size:46px;font-weight:500;color:var(--ink)}
.quote-sub{left:192px;top:2818px;font-size:22px;font-weight:600}
.quote-text{left:192px;top:2860px;width:300px;font-size:12px;line-height:18px;color:var(--text)}
.quote-link{left:192px;top:2950px;padding-bottom:8px;border-bottom:2px solid var(--ink);font-size:13px;font-weight:600;width:100px}
.field{left:600px;width:400px;border:1px solid var(--line);border-radius:22px;padding:12px 18px;font-size:11px;color:var(--muted)}

/* footer */
.footer{left:0;top:3108px;width:1200px;height:480px;background:var(--footer)}
.footer-note{left:192px;top:3200px;width:420px;font-size:16px;line-height:26px;color:var(--white)}
.footer-note b{font-weight:700}
.partner{top:3160px;width:124px;height:124px;background:var(--white);border-radius:6px}
.partner span{position:absolute;left:30px;top:30px;width:64px;height:64px;background:var(--footer)}
.partner.round span{border-radius:50%}
.footer-rule{left:192px;top:3322px;width:816px;height:1px;background:#3b3637}
.footer-small{font-size:11px;line-height:17px;color:#bdb8b9}
.footer-small b{color:var(--white);font-weight:600}
.social{top:3384px;width:30px;height:30px;border-radius:50%;background:#5b5557}
.legal{left:0;top:3488px;width:1200px;height:100px;background:var(--footer-deep)}
.legal p{position:absolute;left:192px;top:18px;width:816px;font-size:9px;line-height:14px;color:#7c7779}
</style>
</head>
<body>

<div class="abs brand">Quarry 9 Pictures</div>
<nav class="abs nav"><span>Home</span><span>About</span><span>Projects</span><span>News</span></nav>
<div class="abs nav-cta">Get in Touch</div>

<div class="abs hero-count">1000</div>
<div class="abs hero-plus">+</div>
<div class="abs section-label" style="top:470px">Projects</div>

<div class="abs tile" role="img" aria-label="Film still: soldier in smoke" style="left:112px;top:592px;width:192px;height:128px;background:linear-gradient(135deg,#5a5148,#2c2824)"><span class="play"></span></div>
<div class="abs tile" role="img" aria-label="Film still: figure in misty forest" style="left:336px;top:720px;width:248px;height:180px;background:linear-gradient(135deg,#a9a49c,#4f4a44)"><span class="play"></span></div>
<div class="abs tile" role="img" aria-label="Film still: dim interior" style="left:176px;top:768px;width:120px;height:92px;background:linear-gradient(135deg,#7a5c4a,#2b211c)"><span class="play"></span></div>
<div class="abs tile" role="img" aria-label="Film still: night street" style="left:416px;top:592px;width:104px;height:80px;background:linear-gradient(135deg,#4a4340,#1d1a19)"><span class="play"></span></div>
<div class="abs tile" role="img" aria-label="Film still: dark cave" style="left:80px;top:888px;width:128px;height:92px;background:linear-gradient(135deg,#3e3a36,#141211)"><span class="play"></span></div>
<div class="abs tile" role="img" aria-label="Film still: battle scene" style="left:240px;top:936px;width:184px;height:144px;background:linear-gradient(135deg,#8c8a88,#353230)"><span class="play"></span></div>
<div class="abs tile" role="img" aria-label="Film still: blue lit spaceship" style="left:464px;top:936px;width:116px;height:96px;background:linear-gradient(135deg,#2a4a6c,#0e1a28)"><span class="play"></span></div>
<div class="abs tile" role="img" aria-label="Film still: dusk landscape" style="left:608px;top:640px;width:128px;height:92px;background:linear-gradient(135deg,#d9d6d2,#6e6a66)"><span class="play"></span></div>
<div class="abs tile" role="img" aria-label="Film still: explosion" style="left:608px;top:760px;width:256px;height:192px;background:linear-gradient(135deg,#e08a34,#6a2c12 60%,#231410)"><span class="play"></span></div>
<div class="abs tile" role="img" aria-label="Film still: starship in space" style="left:768px;top:592px;width:192px;height:144px;background:linear-gradient(135deg,#2d5878,#0b1622)"><span class="play"></span></div>
<div class="abs tile" role="img" aria-label="Film still: aircraft in sky" style="left:984px;top:680px;width:120px;height:96px;background:linear-gradient(135deg,#c9d4dc,#5e6a74)"><span class="play"></span></div>
<div class="abs tile" role="img" aria-label="Film still: desert ruins" style="left:888px;top:816px;width:136px;height:96px;background:linear-gradient(135deg,#d8c49a,#7a6648)"><span class="play"></span></div>
<div class="abs tile" role="img" aria-label="Film still: soldiers on field" style="left:888px;top:936px;width:192px;height:144px;background:linear-gradient(135deg,#8a7e6a,#3a342a)"><span class="play"></span></div>

<div class="abs about-map" role="img" aria-label="Faint world map backdrop"></div>
<h2 class="abs about-title"><span class="heading">About </span><span class="script">Us</span></h2>
<p class="abs about-copy" style="top:1310px">We produce genre feature films, series, documentaries, and anything else that we feel great about. We take pride in our innovative approach to the process of filmmaking and marketing of our produced content. In simple terms, we make good looking motion picture content that is entertaining, visually compelling, and tells a good story.</p>
<p class="abs about-copy" style="top:1462px">Our aim at development of original Canadian content as well as servicing of foreign productions in Toronto, Ontario, Canada.</p>

<div class="abs crew-photo" role="img" aria-label="Camera operator filming on location at sunset"></div>
<h3 class="abs services-title">Experience design &amp; intelligent marketing for growing brands.</h3>
<div class="abs skill" style="top:1786px"><div class="skill-name">Action Movies</div><div class="skill-track"><div class="skill-fill" style="width:64%"></div></div></div>
<div class="abs skill" style="top:1858px"><div class="skill-name">Horror Movies</div><div class="skill-track"><div class="skill-fill" style="width:90%"></div></div></div>
<div class="abs skill" style="top:1930px"><div class="skill-name">Sci-Fi Genre</div><div class="skill-track"><div class="skill-fill" style="width:40%"></div></div></div>
<div class="abs btn" style="left:664px;top:2030px;width:152px;height:40px">Get Quote Today</div>

<h2 class="abs founders-title"><span class="heading">4 </span><span class="script">Founders</span></h2>
<div class="abs arrow" style="left:136px">&#8249;</div>
<div class="abs arrow" style="left:1040px">&#8250;</div>
<div class="abs founder" role="img" aria-label="Portrait of founder Callum" style="left:192px;background:linear-gradient(180deg,#cfcfcf,#6a6a6a)"><span class="founder-name">Callum</span><span class="founder-role">Producer</span></div>
<div class="abs founder" role="img" aria-label="Portrait of founder Dorian" style="left:472px;background:linear-gradient(180deg,#c9c4bd 0%,#9a8f84 55%,#1f8fc4 56%,#1a7fb0 100%)"><span class="founder-name">Dorian</span><span class="founder-role">Director</span></div>
<div class="abs founder" role="img" aria-label="Portrait of founder Efrem" style="left:752px;background:linear-gradient(180deg,#e0e0e0,#5e5e5e)"><span class="founder-name">Efrem</span><span class="founder-role">Writer</span></div>

<h2 class="abs quote-title">Need a Quote?</h2>
<div class="abs quote-sub">Just Ask...</div>
<p class="abs quote-text">Tell us about your project and timeline. Our team will reply within two business days with next steps.</p>
<div class="abs quote-link">Contact Us</div>
<div class="abs field" style="top:2724px;height:40px">Your Name</div>
<div class="abs field" style="top:2776px;height:40px">Email</div>
<div class="abs field" style="top:2828px;height:100px">How can we help you?</div>
<div class="abs btn" style="left:600px;top:2948px;width:112px;height:40px">Submit</div>

<div class="abs footer"></div>
<p class="abs footer-note"><b>Q9P</b> is a child of a partnership between two Canadian companies.</p>
<div class="abs partner" style="left:728px"><span></span></div>
<div class="abs partner round" style="left:884px"><span></span></div>
<div class="abs footer-rule"></div>
<p class="abs footer-small" style="left:192px;top:3380px"><b>(C) 2019 Quarry 9 Pictures Inc.</b><br>All rights reserved.</p>
<p class="abs footer-small" style="left:600px;top:3380px"><b>Q9P Headquarters</b><br>48 Alder Lane, Toronto, ON M5V 2K1<br>Canada</p>
<div class="abs social" style="left:888px"></div>
<div class="abs social" style="left:928px"></div>
<div class="abs social" style="left:968px"></div>
<div class="abs legal"><p>Quarry 9 Pictures and its partners produce and distribute original genre films for audiences worldwide. All titles, stills and trailers shown on this site remain the property of their respective rights holders. Project details and release dates may change without notice. For press or licensing requests please use the contact form above.</p></div>

</body>
</html>
```